Crossfield Holiday Institute needs a webpage design

The worldwide first Crossfield Holiday Institute of the arts - Grenzgängerische Ferienwerkstatt der Formen (in German) - short - GRUV needs a wepage design.
We already have a logo and would need a innovative and dynamic web design in order to be able to launch our website. The website will be our primary marketing tool, so the design should reflect the academy´s mission:
- GRUV offers young artists an experimental platform for experimenting and launching interdisciplinary projects under the guidance of established international artists. GRUV is tomorrow!
Quick facts of the academy:
- worlwide first Crossfield Holiday Institute for professional young artists representing the fine arts: music, dance, literature, visual arts and theatre and not older than 35 years old
- two week long master classes under the guidance of established artists
- set in the beautiful Swiss Alps

Target Market(s)

young artists up to 35 years old

Industry/Entity Type

Artists

Requirements
Must have
• The design should:
- reflect the creed of the academy: GRUV is tomorrow!
- the website will be run in 3 languages: DE, EN and FR, so the simpler the better and cheaper to run
- website needs to include the feature of an digital application from so the applicants can apply online
Nice to have
• Dynamic, flip and turn features to reach the second page
Should not have
• If possible not a traditional design, but futuristic

```html
<!DOCTYPE html>
<html lang="en">
<head>
<meta charset="utf-8">
<title>GRUV – Crossfield Holiday Institute for the Arts</title>
<link rel="stylesheet" href="https://fonts.googleapis.com/css2?family=League+Gothic&family=Arvo:wght@700&family=Roboto:wght@300;400&display=swap">
<style>
  :root {
    --plum: #8e2c87;
    --slate: #6b7173;
    --slate-light: #b7babb;
    --ink-soft: #7d8284;
    --frame: #ffffff;
    --frame-inner: #d9dcdd;
    --rule: #e2e2e2;
    --page: #ffffff;
  }
  * { margin: 0; padding: 0; box-sizing: border-box; }
  html, body { width: 1200px; height: 878px; overflow: hidden; background: var(--page); }
  .page { position: relative; width: 1200px; height: 878px; overflow: hidden; }

  /* brand */
  .brand { position: absolute; left: 173px; top: 78px; display: flex; align-items: center; gap: 12px; }
  .brand-mark { width: 46px; height: 46px; background: var(--plum); border-radius: 6px; }
  .brand-name { font-family: "League Gothic", sans-serif; font-size: 64px; line-height: 1; color: var(--plum); letter-spacing: 1px; }
  .brand-tagline { position: absolute; left: 173px; top: 148px; width: 240px; font-family: "Roboto", sans-serif; font-size: 11px; line-height: 1.3; color: var(--slate); }

  /* headline */
  .headline { position: absolute; left: 520px; top: 90px; font-family: "League Gothic", sans-serif; text-transform: uppercase; line-height: 1; }
  .headline .line-1 { display: block; font-size: 29px; color: var(--slate); }
  .headline .line-1 .faint { color: var(--slate-light); }
  .headline .line-2 { display: block; font-size: 45px; color: var(--slate); margin-top: 2px; }
  .headline .accent { color: var(--plum); }

  /* frame composition */
  .frame {
    position: absolute; background: var(--frame);
    box-shadow: -18px 22px 34px rgba(120,125,130,0.28), 0 2px 4px rgba(0,0,0,0.06);
  }
  .frame::before {
    content: ""; position: absolute; inset: 20px;
    background: linear-gradient(135deg, var(--frame-inner) 0%, #f3f4f4 55%, #ffffff 100%);
    box-shadow: inset 10px -8px 18px rgba(110,115,120,0.25);
  }
  .frame-back   { left: 390px; top: 342px; width: 286px; height: 313px; }
  .frame-small-left { left: 329px; top: 280px; width: 126px; height: 126px; }
  .frame-top    { left: 529px; top: 182px; width: 260px; height: 260px; }
  .frame-corner { left: 838px; top: 192px; width: 126px; height: 125px; }
  .frame-apply  { left: 711px; top: 373px; width: 231px; height: 231px; }
  .frame-low-left { left: 283px; top: 500px; width: 185px; height: 185px; }
  .frame-low-mid  { left: 622px; top: 524px; width: 159px; height: 162px; }
  .frame-low-right { left: 844px; top: 492px; width: 194px; height: 195px; }

  .glyph { position: absolute; font-family: "Arvo", serif; font-weight: 700; line-height: 1; }
  .glyph-h { left: 572px; top: 200px; font-size: 150px; color: var(--slate); }
  .glyph-c { left: 472px; top: 405px; font-size: 200px; color: var(--plum); }
  .glyph-a { left: 770px; top: 420px; font-size: 112px; color: var(--slate); }
  .glyph-g { left: 950px; top: 545px; font-size: 120px; color: var(--plum); }

  .label { position: absolute; font-family: "League Gothic", sans-serif; font-size: 28px; line-height: 1; color: var(--slate); text-decoration: none; }
  .label-institute { left: 572px; top: 326px; }
  .label-crossfield { left: 477px; top: 590px; }
  .label-apply { left: 783px; top: 515px; }

  /* side navigation */
  .side-nav { position: absolute; left: 178px; top: 374px; list-style: none; }
  .side-nav li { display: flex; align-items: center; gap: 9px; height: 43px; }
  .side-nav li::before { content: ""; width: 6px; height: 6px; border-radius: 50%; background: var(--slate); }
  .side-nav a { font-family: "League Gothic", sans-serif; font-size: 25px; color: var(--slate); text-decoration: none; }

  /* mission */
  .mission { position: absolute; left: 201px; top: 728px; display: flex; align-items: center; }
  .mission-title { font-family: "League Gothic", sans-serif; font-size: 42px; color: var(--plum); line-height: 1; }
  .mission-divider { width: 1px; height: 28px; background: var(--slate-light); margin: 0 17px 0 16px; }
  .mission-text { width: 600px; font-family: "Roboto", sans-serif; font-weight: 300; font-size: 12px; line-height: 1.35; color: var(--ink-soft); }

  /* footer */
  .footer { position: absolute; left: 179px; top: 832px; width: 853px; border-top: 1px dotted var(--rule); }
  .copyright { position: absolute; left: 3px; top: 20px; font-family: "Roboto", sans-serif; font-size: 11px; color: var(--slate); }
  .social { position: absolute; right: 4px; top: 19px; display: flex; gap: 9px; list-style: none; }
  .social li { width: 16px; height: 16px; border-radius: 50%; background: #a9adae; }
</style>
</head>
<body>
<main class="page">
  <div class="brand">
    <span class="brand-mark"></span>
    <span class="brand-name">GRUV</span>
  </div>
  <p class="brand-tagline">Grenzgängerische Ferienwerkstatt der Formen</p>

  <h1 class="headline">
    <span class="line-1"><span class="faint">The worldwide</span> first crossfield</span>
    <span class="line-2"><span class="accent">Holiday institute</span> for the arts</span>
  </h1>

  <div class="frame frame-back"></div>
  <div class="frame frame-small-left"></div>
  <div class="frame frame-top"></div>
  <div class="frame frame-corner"></div>
  <div class="frame frame-apply"></div>
  <div class="frame frame-low-left"></div>
  <div class="frame frame-low-mid"></div>
  <div class="frame frame-low-right"></div>

  <span class="glyph glyph-h">h</span>
  <a class="label label-institute" href="#institute">Holiday Institute</a>
  <span class="glyph glyph-c">c</span>
  <a class="label label-crossfield" href="#crossfield">Crossfield</a>
  <span class="glyph glyph-a">a</span>
  <a class="label label-apply" href="#apply">Apply</a>
  <span class="glyph glyph-g">g</span>

  <ul class="side-nav">
    <li><a href="#about">About</a></li>
    <li><a href="#public">Public Attendence</a></li>
    <li><a href="#sponsors">Sponsor &amp; Partners</a></li>
  </ul>

  <section class="mission">
    <h2 class="mission-title">WHAT WE DO?</h2>
    <span class="mission-divider"></span>
    <p class="mission-text">GRUV offers young artists an experimental platform for launching interdisciplinary projects under the guidance of already established international artists. GRUV is tomorrow!</p>
  </section>

  <footer class="footer">
    <p class="copyright">© 2013 GRUVACADEMY.COM. ALL RIGHTS RESERVED.</p>
    <ul class="social" aria-label="Social channels">
      <li></li><li></li><li></li>
    </ul>
  </footer>
</main>
</body>
</html>
```